Business Card Design Project

Create an impressive business care to use
Updates

My logo is available at http://corvalune.example, or

Industry/Entity Type

Business

Requirements
Must have
• company logo

```html
<!DOCTYPE html>
<html lang="en">
<head>
<meta charset="utf-8">
<title>Corvalune Business Cards</title>
<link rel="stylesheet" href="https://fonts.googleapis.com/css2?family=Montserrat:wght@500&family=Arimo&family=Open+Sans:wght@400;600&family=Noto+Serif+SC&display=swap">
<style>
  :root {
    --sheet: #b8bdb5;
    --paper: #ffffff;
    --ink: #111111;
    --green: #86a315;
    --green-soft: #a9c24a;
    --orange: #e06b05;
    --orange-soft: #f4a75c;
    --band-text: #ffffff;
  }
  * { margin: 0; padding: 0; box-sizing: border-box; }
  html, body { width: 1000px; height: 1200px; overflow: hidden; }
  body { background: var(--sheet); position: relative; font-family: "Arimo", Arial, sans-serif; }

  .card {
    position: absolute; left: 36px; width: 928px; height: 536px;
    background: var(--paper); overflow: hidden;
  }
  .card--green { top: 38px; --accent: var(--green); --accent-soft: var(--green-soft); }
  .card--orange { top: 626px; --accent: var(--orange-soft); --accent-soft: var(--orange-soft); }
  .card--orange .contact-band { background: var(--orange); }

  .motif {
    position: absolute; left: 0; top: 0; width: 326px; height: 298px;
    background: radial-gradient(ellipse at 42% 48%, var(--accent) 0%, var(--accent) 55%, rgba(255,255,255,0) 72%);
  }

  .brand {
    position: absolute; left: 368px; top: 62px;
    display: flex; align-items: center; gap: 18px;
  }
  .brand-dot { width: 22px; height: 22px; border-radius: 50%; background: var(--ink); }
  .brand-name {
    font-family: "Montserrat", Arial, sans-serif; font-weight: 500;
    font-size: 66px; letter-spacing: 9px; color: var(--ink); line-height: 1;
  }

  .identity {
    position: absolute; left: 430px; width: 360px; top: 210px;
    text-align: center; color: var(--ink);
  }
  .identity-name { font-size: 28px; line-height: 34px; letter-spacing: -0.3px; }
  .identity-name-zh { font-family: "Noto Serif SC", serif; font-size: 25px; line-height: 34px; letter-spacing: 2px; }
  .identity-title { font-size: 28px; line-height: 34px; }

  .contact-band {
    position: absolute; left: 0; bottom: 0; width: 100%; height: 178px;
    background: var(--green); color: var(--band-text);
    font-family: "Open Sans", Arial, sans-serif;
  }
  .office { position: absolute; top: 24px; }
  .office p { white-space: nowrap; }
  .office a { color: inherit; text-decoration: underline; }
  .office--us { left: 116px; font-size: 13.5px; line-height: 19px; letter-spacing: -0.3px; }
  .office--us .office-line--lg { font-size: 14.5px; }
  .office--cn { left: 458px; font-size: 15.5px; line-height: 22px; font-weight: 600; }
  .office--cn .office-line--zh { font-family: "Noto Serif SC", serif; font-weight: 400; }
</style>
</head>
<body>

<article class="card card--green">
  <div class="motif" role="img" aria-label="Green brush-drawn circles motif"></div>
  <div class="brand"><span class="brand-dot"></span><span class="brand-name">CORVALUNE</span></div>
  <div class="identity">
    <p class="identity-name">Marcus Lee Hanford, PhD</p>
    <p class="identity-name-zh">林晨 博士</p>
    <p class="identity-title">CEO</p>
  </div>
  <footer class="contact-band">
    <div class="office office--us">
      <p>U.S.</p>
      <p>2480 Harbor Crest Way, Suite 210</p>
      <p>Oceanside, CA 92054</p>
      <p class="office-line--lg">Email: <a>mhanford@corvalune.example</a></p>
      <p class="office-line--lg">Cell: 503-555-0142</p>
      <p><a>http://www.corvalune.example</a></p>
    </div>
    <div class="office office--cn">
      <p>China</p>
      <p>1806, NO.42 Linhe Street, Chaoyang District,</p>
      <p>Beijing, China 100020</p>
      <p class="office-line--zh">北京市朝阳区临河街42号晨光中心</p>
      <p><a>http://www.Velmarin.example</a></p>
    </div>
  </footer>
</article>

<article class="card card--orange">
  <div class="motif" role="img" aria-label="Orange brush-drawn circles motif"></div>
  <div class="brand"><span class="brand-dot"></span><span class="brand-name">CORVALUNE</span></div>
  <div class="identity">
    <p class="identity-name">Marcus Lee Hanford, PhD</p>
    <p class="identity-name-zh">林晨 博士</p>
    <p class="identity-title">CEO</p>
  </div>
  <footer class="contact-band">
    <div class="office office--us">
      <p>U.S.</p>
      <p>2480 Harbor Crest Way, Suite 210</p>
      <p>Oceanside, CA 92054</p>
      <p class="office-line--lg">Email: <a>mhanford@corvalune.example</a></p>
      <p class="office-line--lg">Cell: 503-555-0142</p>
      <p><a>http://www.corvalune.example</a></p>
    </div>
    <div class="office office--cn">
      <p>China</p>
      <p>1806, NO.42 Linhe Street, Chaoyang District,</p>
      <p>Beijing, China 100020</p>
      <p class="office-line--zh">北京市朝阳区临河街42号晨光中心</p>
      <p><a>http://www.Velmarin.example</a></p>
    </div>
  </footer>
</article>

</body>
</html>
```